Tidewell Recovery Business Card Design

Professional and clean design. The design colors should flow with the logo. Two-sided card with the website on the back which is:

www.TidewellRecovery.example.

"Specializing in Water Damage Restoration"

On the front I need the name, email, phone, and logo.

Name: Dorian Vashti
Email: Dorian@TidewellRecovery.example
Phone: 555-318-2046 for now

I only have the Preview and Thumbnail right now but should have the source files uploaded within a day or two.

Target Market(s)

Flood victims, home owners with water damage from busted pipes etc...

Industry/Entity Type

Business

Contact Information for Business Card

Name: Dorian Vashti

Font styles to use
Serif
Sans Serif

```html
<!DOCTYPE html>
<html lang="en">
<head>
<meta charset="utf-8">
<title>Tidewell Recovery Business Card</title>
<link href="https://fonts.googleapis.com/css2?family=Cinzel:wght@400;600&family=EB+Garamond:wght@400&display=swap" rel="stylesheet">
<style>
  :root {
    --brand-blue: #2796d6;
    --sky-blue: #5cbde9;
    --pale-blue: rgba(255,255,255,0.12);
    --paper: #ffffff;
    --backdrop: #e9edf0;
    --ink-shadow: rgba(20,40,60,0.18);
  }
  * { margin: 0; padding: 0; box-sizing: border-box; }
  html, body { width: 1200px; height: 780px; overflow: hidden; }
  body {
    background: var(--backdrop);
    display: flex;
    align-items: center;
    justify-content: center;
    gap: 60px;
    font-family: "EB Garamond", serif;
  }
  .card {
    position: relative;
    width: 525px;
    height: 300px;
    overflow: hidden;
    box-shadow: 0 10px 30px var(--ink-shadow);
  }
  /* ---------- back ---------- */
  .card-back { background: var(--brand-blue); color: var(--paper); }
  .back-halo {
    position: absolute;
    width: 300px; height: 300px;
    left: 112px; top: -20px;
    border-radius: 50%;
    background: var(--pale-blue);
  }
  .back-brand {
    position: absolute; inset: 0;
    display: flex; flex-direction: column; align-items: center; justify-content: center;
  }
  .brand-row { display: flex; align-items: center; gap: 14px; }
  .brand-dot { width: 44px; height: 44px; border-radius: 50%; background: var(--paper); }
  .brand-name { font-family: "Cinzel", serif; font-weight: 600; font-size: 38px; letter-spacing: 1px; line-height: 1; }
  .brand-sub {
    display: flex; align-items: center; gap: 8px;
    font-family: "Cinzel", serif; font-weight: 600; font-size: 12px; letter-spacing: 6px;
    margin-top: 4px; margin-left: 58px;
  }
  .brand-sub::before, .brand-sub::after { content: ""; width: 34px; height: 1.5px; background: currentColor; }
  .back-web { font-size: 15px; margin-top: 14px; letter-spacing: 0.3px; }
  /* ---------- front ---------- */
  .card-front { background: var(--paper); color: var(--brand-blue); }
  .front-swoosh { position: absolute; inset: 0; }
  .front-brand { position: absolute; left: 118px; top: 52px; }
  .card-front .brand-dot { background: var(--brand-blue); width: 50px; height: 50px; }
  .card-front .brand-name { font-size: 36px; }
  .holder-name {
    position: absolute; right: 36px; top: 136px;
    font-family: "Cinzel", serif; font-size: 17px; letter-spacing: 1px; color: var(--sky-blue);
  }
  .contact-list {
    position: absolute; right: 36px; top: 172px;
    list-style: none; text-align: right; font-size: 14.5px; line-height: 1.45; color: var(--brand-blue);
  }
  .contact-list li { display: flex; align-items: center; justify-content: flex-end; gap: 8px; }
  .contact-list svg { width: 13px; height: 13px; fill: var(--brand-blue); }
</style>
</head>
<body>
  <section class="card card-back" aria-label="Card back">
    <div class="back-halo"></div>
    <div class="back-brand">
      <div class="brand-row">
        <span class="brand-dot"></span>
        <span class="brand-name">TIDEWELL</span>
      </div>
      <div class="brand-sub">RECOVERY</div>
      <div class="back-web">www.TidewellRecovery.example</div>
    </div>
  </section>

  <section class="card card-front" aria-label="Card front">
    <svg class="front-swoosh" viewBox="0 0 525 300" preserveAspectRatio="none" aria-hidden="true">
      <path d="M0,112 C40,225 200,292 525,300 L0,300 Z" fill="#5cbde9"/>
      <path d="M0,128 C48,235 205,296 525,306 L0,306 Z" fill="#ffffff"/>
      <path d="M0,136 C52,240 205,298 420,300 L0,300 Z" fill="#2796d6"/>
    </svg>
    <div class="front-brand">
      <div class="brand-row">
        <span class="brand-dot"></span>
        <span class="brand-name">TIDEWELL</span>
      </div>
      <div class="brand-sub">RECOVERY</div>
    </div>
    <div class="holder-name">DORIAN VASHTI</div>
    <ul class="contact-list">
      <li>555-318-2046
        <svg viewBox="0 0 24 24"><path d="M6.6 10.8a15 15 0 0 0 6.6 6.6l2.2-2.2a1 1 0 0 1 1-.25 11.4 11.4 0 0 0 3.6.6 1 1 0 0 1 1 1V20a1 1 0 0 1-1 1A17 17 0 0 1 3 4a1 1 0 0 1 1-1h3.5a1 1 0 0 1 1 1c0 1.25.2 2.45.6 3.6a1 1 0 0 1-.25 1z"/></svg>
      </li>
      <li>Dorian@TidewellRecovery.example
        <svg viewBox="0 0 24 24"><path d="M2 5h20v14H2z M4 7v.5l8 5 8-5V7z" fill-rule="evenodd"/></svg>
      </li>
      <li>www.TidewellRecovery.example
        <svg viewBox="0 0 24 24"><path d="M12 2a10 10 0 1 0 0 20 10 10 0 0 0 0-20zm0 2c1.2 1.4 2 3.6 2.2 7H9.8C10 7.6 10.8 5.4 12 4zm-2.2 9h4.4c-.2 3.4-1 5.6-2.2 7-1.2-1.4-2-3.6-2.2-7zM4.1 11a8 8 0 0 1 4.3-6.2A14 14 0 0 0 7.8 11zm0 2h3.7a14 14 0 0 0 .6 6.2A8 8 0 0 1 4.1 13zm12.1 0h3.7a8 8 0 0 1-4.3 6.2 14 14 0 0 0 .6-6.2zm0-2a14 14 0 0 0-.6-6.2 8 8 0 0 1 4.3 6.2z"/></svg>
      </li>
    </ul>
  </section>
</body>
</html>
```